Newsletter Landing Page Design

It's a landing page for a newsletter. Add the form on the landing page.

The landing page aims to drive conversions by encouraging visitors to sign up for the Betting Newsletter. It should convey the value proposition clearly and effectively to attract sports enthusiasts and avid bettors. The design should create a sense of trust, showcase the benefits of subscribing, and guide visitors towards the sign-up process with a user-friendly and visually appealing layout.

Key Elements and Considerations:
The landing page should feature a clean and modern design, utilizing minimalistic aesthetics and intuitive navigation to ensure a seamless user experience. The layout should prominently highlight the unique selling points of the Betting Newsletter, such as expert insights, valuable tips, exclusive promotions, and breaking news updates. Compelling imagery that resonates with the target audience should be incorporated to evoke excitement and credibility. The page should have a responsive design that adapts to different devices and screen sizes, making it accessible to users across platforms. Additionally, trust elements such as testimonials or affiliations with respected experts or organizations should be included to instill confidence. The sign-up process should be user-friendly, capturing essential information without overwhelming visitors. Privacy and data security should be emphasized, and analytics and tracking tools should be implemented for optimization purposes.

By incorporating these elements, the landing page will effectively communicate the value of the Betting Newsletter, provide a seamless user experience, and drive conversions by encouraging visitors to sign up.

Target Market(s)

People looking for Gambling information

Industry/Entity Type

Gambling

Number of Pages Required

1 page

Font styles to use
Sans Serif

Requirements
Must have
• Clean design, modern looking, not elementor looking
Nice to have
• Bold ideas, engaging, and features a human element

```html
<!DOCTYPE html>
<html lang="en">
<head>
<meta charset="utf-8">
<title>Betting Newsletter</title>
<link href="https://fonts.googleapis.com/css2?family=Roboto+Condensed:ital,wght@0,400;0,700;1,700&family=Roboto:wght@400;500;700&display=swap" rel="stylesheet">
<style>
:root{
  --black:#000;
  --ink:#0b0b0b;
  --panel:#141414;
  --yellow:#ffc800;
  --yellow-deep:#e0a000;
  --cream:#faf8f1;
  --grey-bg:#e4e3e0;
  --text-light:#fff;
  --text-muted:#b9b9b9;
  --text-dark:#111;
  --wine:#4a0f12;
}
*{box-sizing:border-box;margin:0;padding:0}
html,body{width:1200px;height:5400px;overflow:hidden}
body{font-family:"Roboto",sans-serif;background:var(--black);color:var(--text-light);position:relative}
.section{position:absolute;left:0;width:1200px;overflow:hidden}
.abs{position:absolute}
.cond{font-family:"Roboto Condensed",sans-serif}
.btn{display:inline-flex;align-items:center;justify-content:center;font-family:"Roboto Condensed",sans-serif;font-weight:700;text-transform:uppercase;border-radius:4px}
.btn-yellow{background:linear-gradient(180deg,var(--yellow),var(--yellow-deep));color:var(--text-dark)}
.btn-white{background:#fff;color:var(--text-dark);font-size:15px;width:86px;height:30px;border-radius:3px}

/* hero */
.hero{top:0;height:745px;background:linear-gradient(90deg,#060606 0%,#0d0b0a 45%,#1a120d 100%)}
.hero-photo{right:0;top:0;width:720px;height:745px;background:radial-gradient(ellipse at 60% 35%,#6b2a14 0%,#3a1a0e 35%,#120c09 70%,#080808 100%)}
.brand{left:113px;top:42px;display:flex;align-items:center;gap:12px;font-family:"Roboto Condensed",sans-serif;font-weight:700;font-size:19px;letter-spacing:.5px}
.brand-mark{width:26px;height:26px;background:var(--yellow)}
.top-actions{right:113px;top:42px;display:flex;gap:12px}
.top-actions .btn{height:32px;font-size:16px;padding:0 14px}
.btn-login{background:#d6d6d6;color:var(--text-dark)}
.hero-title{left:113px;top:178px;font-family:"Roboto Condensed",sans-serif;font-weight:700;font-size:56px;line-height:65px;width:640px}
.hero-title em{color:var(--yellow);font-style:italic}
.hero-text{left:113px;top:420px;font-size:21px;line-height:39px;width:580px}
.signup{left:113px;top:538px;display:flex;gap:8px}
.signup input{width:474px;height:82px;border:2px solid #444;border-radius:4px;background:#ebebeb;font:500 22px "Roboto",sans-serif;padding:0 26px;color:#222}
.signup input::placeholder{color:#222}
.signup .btn{width:308px;height:82px;font-size:23px;letter-spacing:2px}
.hero-gap{top:745px;height:31px;background:#fff}

/* last minute */
.lastmin{top:776px;height:512px;background:var(--cream);color:var(--text-dark)}
.chip{left:113px;top:49px;width:143px;height:143px;border-radius:50%;background:radial-gradient(circle,#8a1a1a 0 45%,#1d2c5a 46% 70%,var(--yellow) 71%)}
.lastmin-title{left:275px;top:58px;font-family:"Roboto Condensed",sans-serif;font-weight:700;font-size:42px;line-height:50px}
.reward-list{left:113px;top:216px;list-style:none;font-family:"Roboto Condensed",sans-serif;font-weight:700}
.reward-list li{position:relative;padding-left:30px;margin-bottom:34px}
.reward-list li::before{content:"";position:absolute;left:0;top:9px;border-left:13px solid var(--text-dark);border-top:8px solid transparent;border-bottom:8px solid transparent}
.reward-list .lead{font-size:25px;line-height:30px}
.reward-list .sub{font-size:21px;line-height:30px}
.reward-list .sub span{color:var(--yellow-deep)}
.lastmin .view{left:113px;top:414px;width:134px;height:50px;font-size:17px}
.lastmin-photo{left:661px;top:51px;width:428px;height:363px;background:linear-gradient(160deg,#2a2220 0%,#5a3a2c 45%,#0f4a2e 85%,#0b2a1b 100%)}

/* benefits */
.benefits{top:1288px;height:772px;background:var(--black)}
.section-title{width:1200px;text-align:center;font-family:"Roboto Condensed",sans-serif;font-weight:700;font-size:42px}
.benefits .section-title{top:72px}
.cards{left:113px;top:174px;display:flex;gap:30px}
.card{position:relative;width:304px;height:437px;background:#8a8a8a;clip-path:polygon(0 0,100% 0,100% 80%,50% 100%,0 80%)}
.card-inner{position:absolute;inset:2px;background:var(--ink);clip-path:polygon(0 0,100% 0,100% 80%,50% 100%,0 80%);text-align:center}
.card-photo{margin:15px 15px 0;height:183px}
.card h3{font-family:"Roboto Condensed",sans-serif;font-weight:700;font-size:29px;margin-top:20px}
.card p{color:var(--text-muted);font-size:20px;line-height:33px;margin:6px 30px 12px}
.benefits .view{left:533px;top:661px;width:134px;height:48px;font-size:17px}

/* promo */
.promo{top:2060px;height:617px;background:radial-gradient(ellipse at 50% 60%,#6a1a18 0%,var(--wine) 45%,#1f0707 100%)}
.promo-box{left:109px;top:76px;width:980px;height:453px;background:rgba(10,8,8,.92);border:2px solid #555;border-radius:6px}
.promo-dash{position:absolute;inset:24px;border:2px dashed #888;border-radius:4px;text-align:center}
.promo h2{font-family:"Roboto Condensed",sans-serif;font-weight:700;font-size:42px;line-height:54px;margin-top:46px}
.promo p{font-size:23px;line-height:33px;margin:18px auto 0;width:700px}
.promo .btn{width:322px;height:71px;font-size:22px;letter-spacing:2px;margin-top:26px}

/* feature */
.feature{top:2677px;height:545px;background:var(--grey-bg)}
.feature-card{left:111px;top:84px;width:974px;height:373px;background:var(--yellow);border:4px solid #fff}
.feature-title{left:159px;top:140px;color:var(--text-dark);font-family:"Roboto Condensed",sans-serif;font-weight:700;font-size:44px;line-height:53px}
.feature-text{left:159px;top:270px;width:420px;color:var(--text-dark);font-size:20px;line-height:33px}
.feature-photo{left:610px;top:48px;width:456px;height:382px;background:radial-gradient(ellipse at 50% 35%,#8a3a1c 0%,#3a1a10 55%,#0e3a26 100%)}

/* news */
.news{top:3222px;height:1070px;background:var(--black)}
.news .section-title{top:100px}
.news-photo{width:462px;height:316px;border:2px solid #cfcfcf;border-radius:6px}
.news-body{width:470px}
.news-body h3{font-family:"Roboto Condensed",sans-serif;font-weight:700;font-size:29px;line-height:44px;text-transform:uppercase}
.meta{display:flex;align-items:center;gap:12px;margin:14px 0 12px;font-family:"Roboto Condensed",sans-serif;font-weight:700;font-size:18px;color:var(--yellow);letter-spacing:1px}
.meta svg{flex:none}
.meta .gap{width:22px}
.news-body p{color:var(--text-muted);font-size:20px;line-height:32px;margin-bottom:18px}

/* about */
.about{top:4292px;height:449px;background:#070707}
.about-box{left:111px;top:57px;width:976px;height:330px;border:2px solid #333;border-radius:6px;background:linear-gradient(90deg,#151515,#0a0a0a)}
.about h2{position:absolute;left:52px;top:62px;font-family:"Roboto Condensed",sans-serif;font-weight:700;font-size:42px}
.about p{position:absolute;left:52px;top:134px;width:490px;color:var(--text-muted);font-size:20px;line-height:32px}
.about-art{position:absolute;right:22px;top:24px;width:400px;height:280px;background:radial-gradient(ellipse at 50% 40%,#7a5210 0%,#2a1c08 50%,transparent 75%)}

/* contact */
.contact{top:4741px;height:659px;background:#090909;text-align:center}
.contact .section-title{top:76px}
.address{top:160px;width:1200px;color:var(--text-muted);font-size:26px}
.phone{top:228px;width:1200px;color:var(--yellow);font-size:36px;display:flex;justify-content:center;align-items:center;gap:14px}
.social{top:326px;width:1200px;display:flex;justify-content:center;gap:36px}
.social span{width:26px;height:26px;border-radius:50%;background:#6c6c6c}
.divider{left:113px;top:408px;width:974px;height:1px;background:#2a2a2a}
.legal{top:460px;width:1200px;color:var(--text-muted);font-size:21px;line-height:33px}
.copy{top:590px;width:1200px;color:var(--text-muted);font-size:21px}
.copy span{color:var(--yellow)}
</style>
</head>
<body>

<header class="section hero">
  <div class="abs hero-photo" role="img" aria-label="Close-up of a spinning roulette wheel in warm low light"></div>
  <div class="abs brand"><span class="brand-mark"></span>BETLINE DIGEST</div>
  <nav class="abs top-actions">
    <a class="btn btn-login">Log in</a>
    <a class="btn btn-yellow">Sign up</a>
  </nav>
  <h1 class="abs hero-title">Subscribe to our <em>Betting Newsletter</em> and never miss latest updates !</h1>
  <p class="abs hero-text">Sign up FREE to receive actionabale insights valuable tips, exclusive promotions, and breaking news updates</p>
  <form class="abs signup">
    <input type="email" placeholder="Enter your E-mail:">
    <button class="btn btn-yellow" type="submit" style="border:2px solid #a97800">Subscribe now</button>
  </form>
</header>
<div class="section hero-gap"></div>

<section class="section lastmin">
  <div class="abs chip" role="img" aria-label="Casino chip badge"></div>
  <h2 class="abs lastmin-title">Last Minute<br>Betting</h2>
  <ul class="abs reward-list">
    <li><div class="lead">Lorem Ipsum is not simply random text.</div><div class="sub">GET A <span>$5</span> REWARD !</div></li>
    <li><div class="lead">Lorem Ipsum is not simply random text.</div><div class="sub">GET A <span>$5</span> REWARD !</div></li>
  </ul>
  <a class="abs btn btn-yellow view">View all</a>
  <div class="abs lastmin-photo" role="img" aria-label="Three friends celebrating a win at a roulette table"></div>
</section>

<section class="section benefits">
  <h2 class="abs section-title">Benefits Of Subscribing</h2>
  <div class="abs cards">
    <article class="card"><div class="card-inner">
      <div class="card-photo" role="img" aria-label="Roulette wheel close-up" style="background:linear-gradient(160deg,#5a2a18,#1e1a16 60%,#0c3a22)"></div>
      <h3>BLACK JACK</h3><p>Many desktop publishing packages and web</p><a class="btn btn-white">More</a>
    </div></article>
    <article class="card"><div class="card-inner">
      <div class="card-photo" role="img" aria-label="Stacks of colourful casino chips and dice" style="background:linear-gradient(90deg,#1d3a8a,#8a1a22 45%,#1a6a2a 70%,#2a4a9a)"></div>
      <h3>BLACK JACK</h3><p>Many desktop publishing packages and web</p><a class="btn btn-white">More</a>
    </div></article>
    <article class="card"><div class="card-inner">
      <div class="card-photo" role="img" aria-label="Hand revealing a pair of aces beside chip stacks" style="background:linear-gradient(90deg,#3a2a2e,#6a1a22 40%,#8a8680 80%)"></div>
      <h3>BLACK JACK</h3><p>Many desktop publishing packages and web</p><a class="btn btn-white">More</a>
    </div></article>
  </div>
  <a class="abs btn btn-yellow view">View all</a>
</section>

<section class="section promo" role="region" aria-label="Reward offer">
  <div class="abs promo-box"><div class="promo-dash">
    <h2>Lorem Ipsum is not simply random text.<br>GET A $5 REWARD !</h2>
    <p>Many desktop publishing packages and web page editors now use Lorem Ipsum as their default model text .</p>
    <a class="btn btn-yellow">Subscribe now</a>
  </div></div>
</section>

<section class="section feature">
  <div class="abs feature-card"></div>
  <h2 class="abs feature-title">Lorem Ipsum is not<br>GET A $5 REWARD !</h2>
  <p class="abs feature-text">Many desktop publishing packages and web page editors now use Lorem Ipsum as their default model text .</p>
  <div class="abs feature-photo" role="img" aria-label="Croupier in a bow tie dealing cards at a green table"></div>
</section>

<section class="section news">
  <h2 class="abs section-title">Latest News</h2>
  <div class="abs news-photo" style="left:113px;top:202px;background:linear-gradient(90deg,#1d2a5a,#7a1a22 45%,#a8a49c 85%)" role="img" aria-label="Chip stacks with a pair of aces"></div>
  <article class="abs news-body" style="left:611px;top:214px">
    <h3>Lorem Ipsum is simply dummy text of the printing</h3>
    <div class="meta">
      <svg width="26" height="26" viewBox="0 0 26 26"><rect x="2" y="4" width="22" height="20" rx="2" fill="none" stroke="#fff" stroke-width="2.5"/><rect x="2" y="4" width="22" height="6" fill="#fff"/><rect x="7" y="1" width="3" height="6" fill="#fff"/><rect x="16" y="1" width="3" height="6" fill="#fff"/></svg>
      25 JAN 2023<span class="gap"></span>
      <svg width="30" height="26" viewBox="0 0 30 26"><rect x="1" y="1" width="19" height="13" rx="2" fill="#fff"/><path d="M5 14 L5 19 L10 14Z" fill="#fff"/><rect x="10" y="9" width="19" height="12" rx="2" fill="#fff" stroke="#000" stroke-width="2"/><path d="M24 21 L24 25 L19 21Z" fill="#fff"/></svg>
      ROSALIND
    </div>
    <p>Many desktop publishing packages and web page editors now use Lorem Ipsum as their default model text .</p>
    <a class="btn btn-white">More</a>
  </article>
  <article class="abs news-body" style="left:115px;top:638px">
    <h3>Lorem Ipsum is simply dummy text of the printing</h3>
    <div class="meta">
      <svg width="26" height="26" viewBox="0 0 26 26"><rect x="2" y="4" width="22" height="20" rx="2" fill="none" stroke="#fff" stroke-width="2.5"/><rect x="2" y="4" width="22" height="6" fill="#fff"/><rect x="7" y="1" width="3" height="6" fill="#fff"/><rect x="16" y="1" width="3" height="6" fill="#fff"/></svg>
      25 JAN 2023<span class="gap"></span>
      <svg width="30" height="26" viewBox="0 0 30 26"><rect x="1" y="1" width="19" height="13" rx="2" fill="#fff"/><path d="M5 14 L5 19 L10 14Z" fill="#fff"/><rect x="10" y="9" width="19" height="12" rx="2" fill="#fff" stroke="#000" stroke-width="2"/><path d="M24 21 L24 25 L19 21Z" fill="#fff"/></svg>
      ROSALIND
    </div>
    <p>Many desktop publishing packages and web page editors now use Lorem Ipsum as their default model text .</p>
    <a class="btn btn-white">More</a>
  </article>
  <div class="abs news-photo" style="left:623px;top:624px;background:radial-gradient(ellipse at 50% 30%,#7a5a2a,#3a2a1a 55%,#0e3a2a)" role="img" aria-label="Woman holding playing cards at a casino table"></div>
</section>

<section class="section about">
  <div class="abs about-box">
    <h2>About us</h2>
    <p>Lorem Ipsum has been the industry's standard dummy text ever since the 1500s, when an unknown printer took a galley of type and scrambled it to make a type specimen book.</p>
    <div class="about-art" role="img" aria-label="Fanned black and gold playing cards with dice"></div>
  </div>
</section>

<footer class="section contact">
  <h2 class="abs section-title">Contact Us</h2>
  <p class="abs address">48 Harbor Lane, Tower Row, Eastfield City, EF-204519</p>
  <p class="abs phone">
    <svg width="20" height="32" viewBox="0 0 20 32"><rect x="2" y="2" width="16" height="28" rx="3" fill="none" stroke="#ffc800" stroke-width="3"/><rect x="7" y="24" width="6" height="2" fill="#ffc800"/></svg>
    1(+00) 5550- 1847
  </p>
  <div class="abs social" aria-label="Social links"><span></span><span></span><span></span><span></span></div>
  <div class="abs divider"></div>
  <p class="abs legal">You're receiving this email because you signed up for «LuckyRiverClub» or<br>attended one of our events. You can unsubscribe from this email or change<br>your email notifications. Online version is here.</p>
  <p class="abs copy">© 2023 <span>Betline Digest</span> | Privacy Policy</p>
</footer>

</body>
</html>
```